Inspiring book cover design (business book for designers and innovators)

I'm writing my first book, to be published early next year. I'm struggling to come up with an inspiring book cover design. I need your help!

Information to be included on the cover:
Book Title: Bright maker's manual
Subtitle: Designing products and services that make sense
Author: Marieke Vollen
Optional (not sure yet if I should include this on the cover): with online toolset

The book will be a square, size 170 x 170 mm
In the uploaded file you can find some example pages from the inside of the book. The cover design should fit with the design style of the example pages. The cover should "jump out" from the shelve in a bookstore and should attract designers, innovators, product managers, developers, and startup founders to buy the book.
Publisher: www.quarlomedia.example

About the book:
Why do some products fail while others become a success? Why do so many companies launch crappy products and services that nobody wants? This book is both a guide to and a source of inspiration for, designing products and services that make sense. Because if they make sense to people, people will want them.
In order for tech products and services to make sense, and create value for users, we need to apply technologies in a meaningful way. We can achieve this by designing strong benefits and at the same time minimizing resistance users might have against new technologies.
This book offers a complete overview of how to develop products and services that make sense: 27 ways to strengthen benefits and 28 ways to mitigate resistance. It offers practical insights, examples, tips, and tools to design products and services that people will love to use.

About the author:
https://www.profilehub.example/in/mariekevollen/

Target Market(s)

designers, innovators, product managers, developers, and startup founders

Industry/Entity Type

Design Agency

Font styles to use
Other font styles liked:
• You can choose. The inside of the book uses 3 fonts: LuloCleanW01-OneBold, Sansation, Segoe UI

Requirements
Must have
• Clean, yet creative design.
Square shape
Fits the design style of the example pages
Sans serif fonts. Do not have to be the same fonts like the ones that are used inside the book (LuloCleanW01-OneBold, Sansation, Segoe UI), but should go well with them.

Bright makers manual
55 ways to design products and services that make sense
Marieke Vollen
Nice to have
• I have several ideas that you might take as a starting point:
1) Do something with the left brain (rational, more digital) - right brain (creative, more emotional). For products to make sense, it needs to appeal to both parts of the brain
2) Work with a pattern, for example a (polygonal) triangular pattern
3) playful element in the letters, for example turning the O in innovator's into an on-off button or a stylish smiley, flipping the N in innovator's, doing something playful with the ' in innovator's
I've uploaded some images as a source of inspiration.

The cover should have a different color than the red/blue used in the example pages, but should fit the color palette that is used in the example pages.
Trigger curiosity.
Should not have
• Photographic pictures

```html
<!DOCTYPE html>
<html lang="en">
<head>
<meta charset="utf-8">
<title>Bright maker's manual – book cover</title>
<link rel="stylesheet" href="https://fonts.googleapis.com/css2?family=Montserrat:wght@800;900&family=Open+Sans:wght@700&display=swap">
<style>
  :root {
    --navy: #000766;
    --royal: #0012b8;
    --electric: #0a2cff;
    --sky: #3d9cff;
    --aqua: #7eeee8;
    --white: #ffffff;
  }
  html, body {
    margin: 0;
    padding: 0;
    width: 1200px;
    height: 1200px;
    overflow: hidden;
    background: var(--navy);
  }
  .cover {
    position: relative;
    width: 1200px;
    height: 1200px;
    overflow: hidden;
  }
  .cover__pattern {
    position: absolute;
    inset: 0;
    background:
      radial-gradient(ellipse 420px 360px at 830px 880px, rgba(126, 238, 232, 0.9), rgba(61, 156, 255, 0.55) 55%, transparent 80%),
      radial-gradient(ellipse 360px 180px at 220px 40px, rgba(80, 180, 255, 0.85), transparent 75%),
      radial-gradient(ellipse 500px 420px at 560px 420px, var(--navy), transparent 75%),
      radial-gradient(ellipse 300px 260px at 1150px 120px, var(--electric), transparent 80%),
      radial-gradient(ellipse 380px 260px at 160px 1140px, rgba(61, 156, 255, 0.8), transparent 80%),
      linear-gradient(160deg, var(--royal) 0%, var(--navy) 45%, var(--electric) 80%, var(--sky) 100%);
  }
  .cover__title {
    position: absolute;
    left: 107px;
    top: 220px;
    margin: 0;
    font-family: "Montserrat", sans-serif;
    font-weight: 900;
    font-size: 126px;
    line-height: 126px;
    letter-spacing: 1px;
    color: var(--white);
    text-transform: uppercase;
  }
  .cover__title span { display: block; }
  .cover__subtitle {
    position: absolute;
    left: 121px;
    top: 666px;
    margin: 0;
    padding-left: 15px;
    border-left: 2px solid var(--white);
    font-family: "Open Sans", sans-serif;
    font-weight: 700;
    font-size: 42px;
    line-height: 49px;
    letter-spacing: -0.5px;
    color: var(--white);
  }
  .cover__author {
    position: absolute;
    left: 483px;
    top: 1074px;
    margin: 0;
    font-family: "Montserrat", sans-serif;
    font-weight: 800;
    font-size: 25px;
    letter-spacing: 6px;
    color: var(--white);
    text-transform: uppercase;
  }
</style>
</head>
<body>
  <main class="cover">
    <div class="cover__pattern" role="img" aria-label="Low-poly triangular pattern in navy, royal blue and aqua tones"></div>
    <h1 class="cover__title">
      <span>Bright</span>
      <span>Maker’s</span>
      <span>Manual</span>
    </h1>
    <p class="cover__subtitle">How to design product<br>and services that make sense</p>
    <p class="cover__author">Marieke Vollen</p>
  </main>
</body>
</html>
```